Business Card Design

Looking for a professional looking business card for a carpentry/construction business that deals with renovations, extensions, homes, and anything carpentry based in Northern Australia. Would like to incorporate the attached logo with backgrounds of white, grey or maybe a close up of timber/wood grain. Thanks

Industry/Entity Type

Carpentry

Contact Information for Business Card

Dean Carlow, Owner, Po Box 2674 Katherine NT 0851, dean-carlow@fernmail.example, 0419563072, Builders Number: 293417CR

Requirements
Should not have
• Power tools/hand tools related to carpentry

```html
<!DOCTYPE html>
<html lang="en">
<head>
<meta charset="utf-8">
<title>Carlow Carpentry – Business Card</title>
<link rel="stylesheet" href="https://fonts.googleapis.com/css2?family=Ubuntu:wght@400;500;700&display=swap">
<style>
  :root {
    --card-bg: #f7f8fa;
    --ink: #23272c;
    --brand-blue: #1b4fd8;
    --accent-sky: #4cc3f2;
    --brick: #a8442f;
    --brick-dark: #7d2f22;
    --timber: #e2c08f;
  }
  html, body {
    margin: 0;
    padding: 0;
    width: 1200px;
    height: 741px;
    overflow: hidden;
    background: var(--card-bg);
  }
  .card {
    position: relative;
    width: 1200px;
    height: 741px;
    background: var(--card-bg);
    font-family: "Ubuntu", sans-serif;
    color: var(--ink);
  }
  .brand {
    position: absolute;
    left: 74px;
    top: 92px;
    display: flex;
    align-items: center;
    gap: 18px;
  }
  .brand-mark {
    width: 22px;
    height: 22px;
    background: var(--accent-sky);
  }
  .brand-name {
    font-size: 64px;
    font-weight: 700;
    color: var(--brand-blue);
    letter-spacing: -0.5px;
    line-height: 1;
  }
  .contact {
    position: absolute;
    left: 65px;
    top: 368px;
  }
  .contact-name {
    font-size: 47px;
    font-weight: 400;
    margin: 0;
    line-height: 1.15;
  }
  .contact-role {
    font-size: 31px;
    margin: 6px 0 0;
    line-height: 1.2;
  }
  .contact-details {
    list-style: none;
    margin: 42px 0 0;
    padding: 0;
    font-size: 30px;
    line-height: 43px;
  }
  .feature-art {
    position: absolute;
    left: 724px;
    top: 346px;
    width: 374px;
    height: 340px;
  }
</style>
</head>
<body>
  <div class="card">
    <div class="brand">
      <span class="brand-mark"></span>
      <span class="brand-name">Carlow Carpentry</span>
    </div>

    <div class="contact">
      <h1 class="contact-name">Dean Carlow</h1>
      <p class="contact-role">Owner</p>
      <ul class="contact-details">
        <li>Po Box 2674 Katherine NT 0851</li>
        <li>E-mail: dean-carlow@fernmail.example</li>
        <li>Phone: 0419563072</li>
        <li>Builders Number: 293417CR</li>
      </ul>
    </div>

    <svg class="feature-art" viewBox="0 0 374 340" role="img" aria-label="Map of Australia filled with red brick wall above and light timber grain below">
      <defs>
        <linearGradient id="brickToTimber" x1="0" y1="0" x2="0" y2="1">
          <stop offset="0" stop-color="var(--brick)"/>
          <stop offset="0.58" stop-color="var(--brick-dark)"/>
          <stop offset="0.66" stop-color="var(--timber)"/>
          <stop offset="1" stop-color="var(--timber)"/>
        </linearGradient>
      </defs>
      <rect x="0" y="0" width="374" height="340" rx="40" fill="url(#brickToTimber)"/>
    </svg>
  </div>
</body>
</html>
```